48207 Velmora Lane Ad (for Facebook and Instagram)

Ad to run on Social Media (i.e. Facebook, Instagram etc.)
to advertise sale of property.

Target Market(s)

Prospective Buyers

Requirements
Must have
• TEXT
• Presenting
• 48207 Velmora Lane, Brandywine, MD
• Priced to Sell
• 5 Bedroom / 4 Bathroom Colonial with Contemporary Design and Charm
• Over 5,000 sq ft of Spacious Elegance
• Extraordinary Master Bedroom with Spacious Bath
• Modern Open Concept Kitchen
• Natural Oak Floors
• Stainless Steel Appliances
• Granite Counter-Tops
• Exterior with Outdoor Security, Design Lighting and Sprinkler System
• Just 10 Minutes From Corvel Landing
• Call Marcus Pelley, Realtor
• Dunmore Realty Inc.
• Phone (240) 555-0183
• Email - premierhomedesk@quillmail.example

```html
<!DOCTYPE html>
<html lang="en">
<head>
<meta charset="utf-8">
<title>48207 Velmora Lane – Listing Ad</title>
<link rel="stylesheet" href="https://fonts.googleapis.com/css2?family=Great+Vibes&family=Montserrat:wght@400;500;600;700;800&display=swap">
<style>
  :root {
    --navy: #1d3b8b;
    --navy-deep: #16306f;
    --sky: #7cc6d6;
    --ink: #1c1c1c;
    --white: #ffffff;
    --snow: #eef1f5;
    --brick: #9a6a4d;
  }
  * { box-sizing: border-box; margin: 0; padding: 0; }
  html, body { width: 1200px; height: 1200px; overflow: hidden; background: var(--white); }
  .ad {
    position: relative;
    width: 1200px;
    height: 1200px;
    background: var(--white);
    font-family: "Montserrat", Arial, sans-serif;
    color: var(--ink);
    overflow: hidden;
  }
  .hero-photo {
    position: absolute;
    left: 0; top: 0;
    width: 1200px; height: 600px;
    background:
      linear-gradient(180deg, rgba(255,255,255,0) 55%, #ffffff 96%),
      linear-gradient(180deg, #d9dde3 0%, #b58a6e 30%, var(--brick) 48%, #c9b6a8 60%, var(--snow) 75%, #ffffff 100%);
  }
  .presenting {
    position: absolute;
    top: 548px; left: 0; width: 100%;
    text-align: center;
    font-family: "Great Vibes", cursive;
    font-weight: 400;
    font-size: 100px;
    line-height: 1;
    color: var(--navy);
  }
  .address {
    position: absolute;
    top: 640px; left: 0; width: 100%;
    text-align: center;
    font-size: 46px;
    font-weight: 500;
    letter-spacing: 1px;
    color: var(--navy);
    text-transform: uppercase;
  }
  .price {
    position: absolute;
    top: 694px; left: 0; width: 100%;
    text-align: center;
    font-size: 30px;
    font-weight: 800;
    letter-spacing: 2px;
    color: var(--sky);
    text-transform: uppercase;
  }
  .divider {
    position: absolute;
    top: 742px; left: 64px;
    width: 1082px; height: 3px;
    background: var(--sky);
  }
  .features {
    position: absolute;
    top: 990px;
    top: 992px;
    list-style: none;
    font-size: 19px;
    line-height: 30px;
    color: var(--ink);
  }
  .features { top: 990px; }
  .features--left, .features--right { top: 994px; }
  .features--left { top: 994px; }
  .features li { position: relative; padding-left: 16px; margin-bottom: 4px; }
  .features li::before { content: "•"; position: absolute; left: 0; }
  .features--left { left: 64px; width: 330px; top: 994px; }
  .features--right { left: 453px; width: 380px; }
  .features--right li { margin-bottom: 9px; }
  .features--left, .features--right { top: 994px; }
  .features--left, .features--right { top: 994px; }
  .feature-block { position: absolute; top: 994px; }
  .area-photo {
    position: absolute;
    left: 838px; top: 770px;
    width: 308px; height: 204px;
    overflow: hidden;
    background: linear-gradient(180deg, #2b2a5c 0%, #5b3f7a 45%, #c26a8a 62%, #2c3f6d 78%, #1a2446 100%);
  }
  .area-tag {
    position: absolute;
    left: 60px; top: 22px;
    width: 280px;
    transform: rotate(15deg);
    transform-origin: center;
    background: var(--sky);
    color: var(--navy-deep);
    font-size: 10px;
    font-weight: 700;
    text-align: center;
    white-space: nowrap;
    padding: 4px 0;
    letter-spacing: 0.5px;
  }
  .brand-name {
    position: absolute;
    left: 48px; top: 1036px;
    width: 463px;
    font-size: 54px;
    font-weight: 700;
    line-height: 1.05;
    color: var(--navy);
    text-align: center;
    text-transform: uppercase;
    letter-spacing: 2px;
  }
  .agent {
    position: absolute;
    left: 541px; top: 1032px;
    width: 350px;
  }
  .agent-name {
    font-size: 27px;
    font-weight: 700;
    line-height: 1.15;
    color: var(--ink);
  }
  .contact {
    display: flex;
    align-items: center;
    gap: 8px;
    font-weight: 700;
    color: var(--ink);
  }
  .contact--phone { font-size: 25px; margin-top: 10px; }
  .contact--email { font-size: 15px; margin-top: 4px; white-space: nowrap; }
  .contact svg { flex: none; }
  .member-badge {
    position: absolute;
    left: 826px; top: 1038px;
    width: 42px; height: 50px;
    background: var(--navy);
  }
  .agent-photo {
    position: absolute;
    left: 940px; top: 990px;
    width: 260px; height: 179px;
    background: linear-gradient(180deg, #ececec 0%, #d7d7d7 55%, #2a2a2a 100%);
  }
  .base-band {
    position: absolute;
    left: 0; bottom: 0;
    width: 1200px; height: 31px;
    background: var(--navy);
  }
</style>
</head>
<body>
<main class="ad">
  <div class="hero-photo" role="img" aria-label="Photo of a brick colonial house with dormer windows in a snowy wooded lot"></div>

  <h2 class="presenting">Presenting</h2>
  <h1 class="address">48207 Velmora Lane, Brandywine, MD</h1>
  <p class="price">Priced to Sell Only $550,000</p>
  <div class="divider"></div>

  <ul class="features features--left" style="top:770px">
    <li>5 Bedroom / 4 Bathroom Colonial with Contemporary Design and Charm</li>
    <li>Over 5,000 sq ft of Spacious Elegance</li>
    <li>Extraordinary Master Bedroom with Spacious Bath</li>
  </ul>
  <ul class="features features--right" style="top:770px">
    <li>Modern Open Concept Kitchen</li>
    <li>Natural Oak Floors</li>
    <li>Stainless Steel Appliances</li>
    <li>Granite Counter-Tops</li>
    <li>Exterior with Outdoor Security, Design Lighting &amp; Sprinkler System</li>
  </ul>

  <div class="area-photo" role="img" aria-label="Night photo of the Corvel Landing waterfront with a lit Ferris wheel">
    <span class="area-tag">10 MINS FROM CORVEL LANDING</span>
  </div>

  <div class="brand-name">Dunmore<br>Realty Inc.</div>

  <div class="agent">
    <p class="agent-name">Marcus Pelley,<br>REALTOR</p>
    <p class="contact contact--phone">
      <svg width="20" height="20" viewBox="0 0 20 20" aria-hidden="true"><circle cx="10" cy="10" r="10" fill="#1d3b8b"/><path d="M7 5.5l1.6 2.2-1 1.1c.6 1.3 1.6 2.3 2.9 2.9l1.1-1 2.2 1.6-.8 1.9c-3.8-.2-6.9-3.3-7.1-7.1z" fill="#fff"/></svg>
      (240) 555-0183
    </p>
    <p class="contact contact--email">
      <svg width="18" height="18" viewBox="0 0 20 20" aria-hidden="true"><circle cx="10" cy="10" r="10" fill="#1d3b8b"/><rect x="5" y="6.5" width="10" height="7" fill="none" stroke="#fff" stroke-width="1.3"/><path d="M5 6.5l5 4 5-4" fill="none" stroke="#fff" stroke-width="1.3"/></svg>
      premierhomedesk@quillmail.example
    </p>
  </div>

  <div class="member-badge" aria-hidden="true"></div>

  <div class="agent-photo" role="img" aria-label="Portrait of agent Marcus Pelley in a dark suit"></div>

  <div class="base-band"></div>
</main>
</body>
</html>
```